BrightvaleCare.com, a web based eHealth startup, needs a URL landing page.

We will be building a portfolio of mocked up website screen shots of our products that we will use to engage prospective customers. We would like to start with the company's URL landing page in order to quickly capture a client's interest and identify a graphic artist that we think has the understanding of the feel/UI we are looking for and the talent to meet our expectations. The two solutions we would like to showcase are "BrightvaleConnectLink" (BCL) and "BrightvaleCircles" (BCS).

BCL is a product for improving hospital inpatient communication using tablets and smart phones. Key descriptors for this solution would be, "Improve communication between the patient, the health care team, and the family care team", "Improve communication between Health Team members", and "Monitor for success and improvement opportunities of administrative goals using direct patient feedback."

BCS is a product for improving patient communication after discharge using tablets, smart phones, and computers. Key descriptors for this solution would be, "Transition support to the Family Care Team", "Stay connected after discharge by creating a VitaCircle of support", and "Monitor progress, provide encouragement, and coordinate support of loved ones"

The goal of the site will be to give potential customers the impression/feeling of great communication, happiness, and health to patients and staff in the hospital and patients, family, and health care providers outside of the hospital. We are hoping to build a relationship with a talented graphic artist as we continue to grow.
Updates

                                        Hello all, I'm trying to upload a logo file to the project brief, but I'm having a little trouble. I have contacted customer service to request a little help. I will also try and find some examples of pages that may have the look I was thinking of. I didn't try to find anything at the start of the project because I was interested to see if there was a design that I may not have thought of. I can certainly try to find some examples though. As for the logo, I tried to put something together on Photoshop, though I also did one on PowerPoint. All I did for now was use BrightvaleCare where the My was in freestyle script, Health was in Adobe Caslon, the e at the end of Health was in freestyle script again, and the Solutions was in Adobe Caslon again. I also made the freestyle script a bright blue and the Adobe Caslon black in color. This was just what I tried first. Underneath the script I had three circles overlapping so that the point at which they all intersected was in the shape of a shield. This symbol stood for "patient centered care". I guess I'll be posting a project for a logo design soon as well to help refine this. This is my first time using a design site like this so I apologize if there is information needed that I have not provided in a easy to use format. I will certainly extend the deadline if more time is needed.  Thank you and please feel free to send any messages or comments. Thanks again.  

Industry/Entity Type

Building

Requirements
Must have
• A banner with scrolling pictures depicting scenes of patients of all ages happily interacting with hospital health team members, people (patients and nurses/doctors) using tablets, smart phones, and computers in the in the hospital, and patients (elderly and 10-15 years old) using happily using a tablet, smart phone, and/or computer.
• Clean, clutter free look.
• Buttons for [Home], [Solutions], [Platform Model], and [Contact Us].

```html
<!DOCTYPE html>
<html lang="en">
<head>
<meta charset="UTF-8">
<title>BrightvaleCare</title>
<link href="https://fonts.googleapis.com/css2?family=Rokkitt:wght@400&display=swap" rel="stylesheet">
<style>
  :root {
    --page-bg: #ffffff;
    --brand-blue: #3e6282;
    --brand-red: #d92525;
    --brand-grey: #7a7a7a;
    --button-text: #ffffff;
  }
  html, body {
    margin: 0;
    padding: 0;
    overflow: hidden;
    background: var(--page-bg);
  }
  .landing {
    position: relative;
    width: 1200px;
    height: 900px;
    background: var(--page-bg);
    overflow: hidden;
    font-family: "Rokkitt", Georgia, serif;
  }
  .brand {
    position: absolute;
    left: 0;
    top: 380px;
    width: 1200px;
    display: flex;
    justify-content: center;
    align-items: center;
    gap: 18px;
  }
  .brand-dot {
    width: 70px;
    height: 70px;
  }
  .brand-name {
    margin: 0;
    font-weight: 400;
    font-size: 84px;
    line-height: 1;
    color: var(--brand-blue);
  }
  .main-nav {
    position: absolute;
    top: 555px;
    left: 240px;
    width: 717px;
    height: 59px;
  }
  .nav-button {
    position: absolute;
    top: 0;
    height: 59px;
    border-radius: 15px;
    display: flex;
    align-items: center;
    justify-content: center;
    color: var(--button-text);
    font-size: 25px;
    text-decoration: none;
  }
  .nav-solutions { left: 0; width: 222px; background: var(--brand-red); }
  .nav-platform  { left: 252px; width: 222px; background: var(--brand-blue); }
  .nav-contact   { left: 495px; width: 222px; background: var(--brand-grey); }
</style>
</head>
<body>
  <main class="landing">
    <header class="brand">
      <svg class="brand-dot" viewBox="0 0 70 70" aria-hidden="true">
        <circle cx="35" cy="35" r="33" fill="#e68a8a"/>
      </svg>
      <h1 class="brand-name">BrightvaleCare</h1>
    </header>
    <nav class="main-nav">
      <a class="nav-button nav-solutions" href="#solutions">Solutions</a>
      <a class="nav-button nav-platform" href="#platform">Platform Model</a>
      <a class="nav-button nav-contact" href="#contact">Contact BCL</a>
    </nav>
  </main>
</body>
</html>
```